Create a book cover - front, back and spine - for a book aimed at high school and college graduates. The book poses a series of questions and possible ways of answering these questions.

Size 5" x 8" with a .45" spine.

Target Market(s)

18-25 year old high school and college graduates.

Industry/Entity Type

High School

Requirements
Must have
• Front cover - image(s) related to graduation, text "Seven Crossroads Before Your Next Chapter" and the author "Tomas Quillan"

Back cover - see attachment. Text will be altered later but right now I just need filler spots.

```html
<!DOCTYPE html>
<html lang="en">
<head>
<meta charset="utf-8">
<title>Seven Crossroads Before Your Next Chapter – Cover</title>
<link href="https://fonts.googleapis.com/css2?family=Oswald:wght@600;700&family=Carlito:ital,wght@0,400;0,700;1,700&family=Tinos&display=swap" rel="stylesheet">
<style>
  :root {
    --paper: #ffffff;
    --ink: #1a1a1a;
    --red: #e8141c;
    --blue: #1f5fc8;
    --photo-dark: #2c3a2a;
    --photo-mid: #6d7a5f;
    --photo-light: #c9c4b8;
  }
  html, body { margin: 0; padding: 0; overflow: hidden; background: var(--paper); }
  .cover {
    position: relative;
    width: 1200px; height: 914px;
    background: var(--paper);
    overflow: hidden;
    font-family: "Carlito", "Calibri", sans-serif;
    color: var(--ink);
  }
  /* Back cover */
  .back { position: absolute; left: 60px; top: 52px; width: 468px; }
  .lead-quote { margin: 0; }
  .lead-quote .headline {
    font-style: italic; font-weight: 700; color: var(--red);
    font-size: 24px; line-height: 30px;
  }
  .lead-quote .rest { font-size: 13.5px; line-height: 17px; }
  .lead-quote .who { font-size: 12.5px; color: var(--red); margin-top: 3px; padding-left: 6px; }
  .who b { font-weight: 700; }
  .teaser { color: var(--blue); font-size: 17px; line-height: 19px; margin: 19px 0 0; }
  .blurb { font-size: 16.3px; line-height: 19px; margin: 18px 0 0; }
  .blurb p { margin: 0 0 6px; }
  .praise { margin-top: 38px; font-size: 12.3px; line-height: 18px; }
  .praise blockquote { margin: 0 0 17px; }
  .praise .who { color: var(--blue); margin-top: 2px; padding: 0; font-size: 12.3px; }
  .praise .who b { color: var(--red); }
  /* Spine and front */
  .spine, .front-title, .front-author { position: absolute; }
  .spine { left: 570px; top: 0; width: 60px; height: 914px; }
  .front-title { left: 672px; top: 48px; width: 475px; height: 600px; }
  .front-photo {
    position: absolute; left: 805px; top: 648px; width: 290px; height: 215px;
    background: radial-gradient(ellipse at 50% 45%, #3b4660 0%, #6b6e7e 45%, rgba(255,255,255,0) 72%);
  }
  .front-author {
    left: 690px; top: 806px; width: 440px; text-align: center;
    font-family: "Tinos", "Times New Roman", serif; font-size: 34px; letter-spacing: 7px;
  }
</style>
</head>
<body>
<div class="cover">

  <section class="back">
    <div class="lead-quote">
      <div class="headline">“This was one of the best books I ever read</div>
      <div class="rest">because it had consonants and vowels and a variety of punctuation marks!”</div>
      <div class="who"><b>Dwayne Pellick,</b> Coastal Plains University – Class of 2013</div>
    </div>
    <p class="teaser">Should you get married? How will you invest? Do you believe the world is ruled by randomness? How many Pagebook friends do you have? Should you tell a stranger he has broccoli in his teeth? Do you objectify yourself?</p>
    <div class="blurb">
      <p>You might have thought you left behind the world of high anxiety testing the moment you donned your commencement robe and cap, and accepted your diploma on a stage far, far away.</p>
      <p>Ahhh…the naiveté of youth. But as you walked deeper into the adult world, you’ve since realized that it is the questions of life that truly kick you in the arse (and life’s retake policy isn’t nearly as generous as your teacher’s).</p>
      <p>Using evidence from history, psychology, economics, literature, and a lifetime of answering incorrectly, Tomas Quillan throws out the key questions all graduates must face, while giving you the ammunition you’ll need to choose wisely.</p>
    </div>
    <div class="praise">
      <blockquote>“If only I’d have answered these questions after I’d graduated, I might not be living in my parents basement trying to invent a new synonym for ‘fetch’”
        <div class="who"><b>-Marla Fenwick,</b> Very Important College – Class of 2046</div></blockquote>
      <blockquote>“This book has just the right balance of history and economics and totally made up stuff that it makes his theories both palpable and alluring to Type 1 Diabetics and furniture salesmen.”
        <div class="who"><b>-Reggie Tolliver,</b> Birchwood University – Class of 2008</div></blockquote>
      <blockquote>“A great book! I’ll read it in a few weeks if I have nothing else to do! I like exclamation marks!”
        <div class="who"><b>-Polly Pennington,</b> Linden Hollow High School, Class of 2012</div></blockquote>
    </div>
  </section>

  <svg class="spine" viewBox="0 0 60 914" aria-label="Spine">
    <text transform="translate(22 55) rotate(90)" font-family="Oswald, sans-serif" font-weight="700" font-size="28" textLength="530" lengthAdjust="spacingAndGlyphs"><tspan fill="var(--red)">Seven Crossroads </tspan><tspan fill="var(--blue)">Before Your Next Chapter</tspan></text>
    <text transform="translate(22 680) rotate(90)" font-family="Tinos, serif" font-size="24" fill="var(--red)" textLength="180" lengthAdjust="spacing">TOMAS QUILLAN</text>
  </svg>

  <svg class="front-title" viewBox="0 0 475 600" aria-label="Seven Crossroads Before Your Next Chapter">
    <defs>
      <linearGradient id="photoTone" x1="0" y1="0" x2="1" y2="1">
        <stop offset="0" stop-color="var(--photo-light)"/>
        <stop offset="0.45" stop-color="var(--photo-mid)"/>
        <stop offset="1" stop-color="var(--photo-dark)"/>
      </linearGradient>
    </defs>
    <g role="img" aria-label="Numeral 7 filled with a photo of a smiling graduate in cap and gown raising a diploma">
      <text x="237" y="342" text-anchor="middle" font-family="Oswald, sans-serif" font-weight="700" font-size="430" fill="url(#photoTone)">7</text>
    </g>
    <text x="8" y="445" font-family="Oswald, sans-serif" font-weight="700" font-size="100" fill="var(--red)" textLength="460" lengthAdjust="spacingAndGlyphs">CROSSROADS</text>
    <text x="8" y="522" font-family="Oswald, sans-serif" font-weight="700" font-size="64" fill="var(--blue)" textLength="460" lengthAdjust="spacingAndGlyphs">BEFORE YOUR NEXT</text>
    <text x="8" y="592" font-family="Oswald, sans-serif" font-weight="700" font-size="64" fill="var(--blue)" textLength="460" lengthAdjust="spacingAndGlyphs">CHAPTER</text>
  </svg>

  <div class="front-photo" role="img" aria-label="Photo of a young woman in glasses lying on her stomach behind a laptop, thinking"></div>
  <div class="front-author">TOMAS QUILLAN</div>

</div>
</body>
</html>
```